13 Tavo - new website design project

Our company Tavo Electrical is developing a new lead generation website focused on Electrical, LED Lighting and Solar Power. We need a high converting website.

Example of our current website is www.tavoelectrical.com.au You can take content from this website for this new design. Our colours are red, black and white. For our new website we would like to promote Tavo, Bright Days Ahead. Please listen to the jingle.

The below link is the company jingle that we have developed.
http://www.tunecraftaudio.com.au/tav-tc-v1/

The key for this brief is to generate leads for Electrical, LED Lighting (for commercial) and Solar Power & Storage.

Target Market(s)

Business owners in Melbourne Victoria

Number of Pages Required

4 page

Colors
ec1f27
ffffff

Requirements
Must have
• This page must be clean, be in line with company branding and a high converting lead website.

```html
<!DOCTYPE html>
<html lang="en">
<head>
<meta charset="utf-8">
<title>Tavo Electrical – Electrical, LED Lighting & Solar Power</title>
<link href="https://fonts.googleapis.com/css2?family=Lato:wght@400;700&family=Raleway:wght@400;500;600;700&display=swap" rel="stylesheet">
<style>
:root{
  --red:#ec1f27;
  --ink:#222222;
  --text:#555555;
  --muted:#777777;
  --line:#dddddd;
  --grey-bg:#f1f1f1;
  --dark:#2b2b2b;
  --darker:#1c1c1c;
  --white:#ffffff;
}
*{box-sizing:border-box;margin:0;padding:0}
html,body{width:1200px;height:3409px;overflow:hidden}
body{font-family:'Lato',sans-serif;color:var(--text);background:var(--white);position:relative}
.abs{position:absolute}
h1,h2,h3,h4{font-family:'Raleway',sans-serif;font-weight:600;color:var(--ink)}
.red{color:var(--red)}

/* header */
.site-header{position:absolute;top:0;left:0;width:1200px;height:141px;background:var(--white)}
.brand{position:absolute;left:52px;top:22px;display:flex;align-items:center;gap:12px}
.brand-dot{width:44px;height:44px;border-radius:50%;background:var(--red)}
.brand-name{font-family:'Raleway',sans-serif;font-weight:700;font-size:46px;color:var(--ink);letter-spacing:1px;line-height:1}
.brand-tag{position:absolute;left:78px;top:104px;font-family:'Raleway',sans-serif;font-size:16px;font-weight:600;color:var(--ink)}
.contact-tab{position:absolute;right:0;top:0;height:46px;width:430px;background:var(--red);color:var(--white);display:flex;align-items:center;gap:16px;padding-left:40px;font-size:16px;font-weight:700;clip-path:polygon(24px 0,100% 0,100% 100%,0 100%)}
.contact-tab span{display:flex;align-items:center;gap:8px}
.contact-tab .sep{width:1px;height:24px;background:rgba(255,255,255,.6)}
.main-nav{position:absolute;right:52px;top:104px;display:flex;gap:28px;font-family:'Raleway',sans-serif;font-weight:600;font-size:16px;color:var(--ink)}
.main-nav .active{color:var(--red);border:1px solid var(--red);padding:2px 6px;margin-top:-3px;border-radius:3px}

/* hero */
.hero{position:absolute;top:141px;left:0;width:1200px;height:518px;background:linear-gradient(180deg,#4a5058 0%,#8a8e92 35%,#b3a898 60%,#6b5a48 100%)}
.hero-shade{position:absolute;inset:0;background:linear-gradient(180deg,rgba(0,0,0,0) 55%,rgba(0,0,0,.55) 100%)}
.hero-title{position:absolute;top:398px;width:100%;text-align:center;font-family:'Raleway',sans-serif;font-size:39px;font-weight:500;color:var(--red);letter-spacing:2px}
.hero-title .dot{color:var(--white);margin:0 18px}
.hero-sub{position:absolute;top:455px;width:100%;text-align:center;font-family:'Raleway',sans-serif;font-size:28px;font-weight:500;color:var(--white)}
.hero-arrow{position:absolute;top:222px}

/* welcome */
.welcome-logo{position:absolute;left:57px;top:740px;width:318px;height:170px}
.welcome-logo .brand-name{font-size:96px}
.welcome-logo .brand-dot{width:70px;height:70px}
.welcome-logo .brand-tag{position:static;font-size:30px;margin-top:10px;margin-left:82px}
.v-divider{position:absolute;left:409px;top:700px;width:1px;height:220px;background:var(--line)}
.welcome-title{position:absolute;left:446px;top:702px;font-size:38px}
.welcome-title small{font-size:15px;color:var(--ink);font-weight:600}
.welcome-text{position:absolute;left:448px;top:782px;width:700px;font-size:15.5px;line-height:27px;color:var(--text)}
.btn-outline{position:absolute;left:448px;top:913px;width:152px;height:33px;border:2px solid #555;font-family:'Raleway',sans-serif;font-size:13px;font-weight:700;color:var(--ink);display:flex;align-items:center;justify-content:center;letter-spacing:.5px}

/* services */
.service{position:absolute;top:1007px;width:332px;text-align:center}
.service .photo{width:100%;height:239px;border:2px solid #e6e6e6}
.service h3{margin-top:34px;font-size:22px;font-weight:500;letter-spacing:.5px}
.service p{margin-top:10px;font-size:15px;line-height:24px;color:var(--muted);padding:0 10px}
.service .toggle{width:27px;height:27px;background:#555;color:var(--white);margin:22px auto 0;display:flex;align-items:center;justify-content:center;font-size:22px;line-height:1}
.service .toggle.on{background:var(--red)}
.section-rule{position:absolute;left:0;width:1200px;height:1px;background:var(--line)}

/* section titles */
.sec-title{position:absolute;width:100%;text-align:center;font-size:38px}
.sec-title::after{content:"";display:block;width:270px;height:2px;background:var(--red);margin:10px auto 0}

/* why */
.feature{position:absolute;top:1623px;width:230px;text-align:center}
.feature .icon{width:100px;height:100px;margin:0 auto;border-radius:50%;border:2px solid #ddd;background:var(--white);display:flex;align-items:center;justify-content:center}
.feature h4{margin-top:30px;font-family:'Lato',sans-serif;font-weight:700;font-size:15px;line-height:17px;color:var(--ink);height:36px}
.feature p{margin-top:10px;font-size:14px;line-height:21px;color:var(--ink)}
.feature p b{color:var(--red);font-weight:400}

/* works */
.works-bg{position:absolute;top:1887px;left:0;width:1200px;height:586px;background:var(--grey-bg)}
.work{position:absolute;top:2030px;width:348px;text-align:center}
.work .card{height:210px;background:var(--white);border:1px solid #ddd;box-shadow:0 3px 5px rgba(0,0,0,.15);padding:8px}
.work .mark{height:78px;display:flex;align-items:center;justify-content:center;font-family:'Raleway',sans-serif;font-weight:600;font-size:38px}
.work .photo{height:106px}
.work h4{margin-top:34px;font-family:'Raleway',sans-serif;font-size:21px;font-weight:700;color:var(--red)}
.work .loc{font-size:14px;color:var(--ink);margin-top:4px}
.work p{margin-top:12px;font-size:15px;line-height:21px;color:var(--ink);padding:0 20px}

/* clients */
.client{position:absolute;top:2614px;height:96px;border:1px solid #ddd;background:var(--white);display:flex;align-items:center;justify-content:center;font-family:'Raleway',sans-serif;font-weight:600;font-size:30px}
.client.solid{border:none;background:var(--red);color:var(--white)}
.client.outline{color:var(--red)}
.client-arrow{position:absolute;top:2640px}

/* commitment */
.commit-bg{position:absolute;top:2764px;left:0;width:1200px;height:400px;background:var(--grey-bg)}
.col-title{position:absolute;top:2813px;font-size:28px;font-weight:600}
.col-title::after{content:"";display:block;width:100%;height:1px;background:var(--line);margin-top:10px}
.commit-text{position:absolute;left:52px;top:2876px;width:520px;font-size:14.5px;line-height:27px;color:var(--ink)}
.ticks{position:absolute;left:52px;top:2975px;list-style:none;font-size:14.5px;color:var(--ink)}
.ticks li{display:flex;align-items:center;gap:12px;height:38px}
.quote-box{position:absolute;left:636px;top:2882px;width:512px;height:164px;background:var(--white);border:1px solid #ddd;padding:22px 28px 0 42px;font-size:14px;line-height:26px;color:var(--ink)}
.quote-box::after{content:"";position:absolute;left:50px;bottom:-14px;width:26px;height:26px;background:var(--white);border-right:1px solid #ddd;border-bottom:1px solid #ddd;transform:rotate(45deg)}
.quote-mark{position:absolute;left:12px;top:6px;font-family:Georgia,serif;font-size:48px;color:#bbb}
.avatar{position:absolute;left:662px;top:3064px;width:68px;height:68px;border-radius:50%;background:linear-gradient(160deg,#e8a845,#b86c2c)}
.client-name{position:absolute;left:755px;top:3089px;font-size:15px;font-weight:700;color:var(--red)}

/* footer */
.footer-nav{position:absolute;top:3164px;left:0;width:1200px;height:75px;background:var(--red)}
.footer-links{position:absolute;left:52px;top:26px;display:flex;font-family:'Raleway',sans-serif;font-weight:700;font-size:15px;color:var(--white)}
.footer-links span{padding:0 14px;border-right:1px solid rgba(255,255,255,.6)}
.footer-links span:first-child{padding-left:0}
.footer-links span:last-child{border-right:none}
.social{position:absolute;right:52px;top:20px;display:flex;gap:14px}
.social span{width:34px;height:34px;border:2px solid var(--white);border-radius:50%;color:var(--white);font-size:11px;font-weight:700;display:flex;align-items:center;justify-content:center}
.footer-main{position:absolute;top:3239px;left:0;width:1200px;height:125px;background:var(--dark);color:#ddd}
.f-item{position:absolute;top:32px;display:flex;gap:16px;font-size:14px;line-height:22px}
.f-item b{color:var(--white)}
.f-icon{width:34px;height:34px;border-radius:50%;border:2px solid var(--red);display:flex;align-items:center;justify-content:center;flex:none}
.f-brand{position:absolute;right:52px;top:28px;text-align:right}
.f-brand .name{font-family:'Raleway',sans-serif;font-weight:700;font-size:40px;color:var(--white);line-height:1}
.f-brand .tag{font-family:'Raleway',sans-serif;font-size:14px;color:var(--white);margin-top:4px}
.copyright{position:absolute;top:3364px;left:0;width:1200px;height:45px;background:var(--darker);color:#ccc;font-size:13px;display:flex;align-items:center;justify-content:center}
</style>
</head>
<body>

<header class="site-header">
  <div class="brand"><div class="brand-dot"></div><div class="brand-name">TAVO</div></div>
  <div class="brand-tag">Bright Days Ahead</div>
  <div class="contact-tab">
    <span><svg width="16" height="16" viewBox="0 0 24 24"><path fill="#fff" d="M6.6 10.8a15 15 0 0 0 6.6 6.6l2.2-2.2a1 1 0 0 1 1-.25 11.4 11.4 0 0 0 3.6.57 1 1 0 0 1 1 1V20a1 1 0 0 1-1 1A17 17 0 0 1 3 4a1 1 0 0 1 1-1h3.5a1 1 0 0 1 1 1c0 1.25.2 2.45.57 3.57a1 1 0 0 1-.25 1z"/></svg>138420</span>
    <span class="sep"></span>
    <span><svg width="18" height="14" viewBox="0 0 18 14"><rect x="1" y="1" width="16" height="12" fill="none" stroke="#fff" stroke-width="1.6"/><path d="M1 1l8 7 8-7" fill="none" stroke="#fff" stroke-width="1.6"/></svg>service@tavoelectrical.com.au</span>
  </div>
  <nav class="main-nav">
    <span class="active">HOME</span><span>TAVO STORY</span><span>SERVICES</span><span>OUR WORK</span><span>CONTACT US</span>
  </nav>
</header>

<section class="hero" role="img" aria-label="Interior of a large industrial warehouse with new high-bay lighting">
  <div class="hero-shade"></div>
  <svg class="hero-arrow" style="left:18px" width="24" height="48" viewBox="0 0 24 48"><path d="M20 4L4 24l16 20" fill="none" stroke="rgba(255,255,255,.6)" stroke-width="3"/></svg>
  <svg class="hero-arrow" style="right:18px" width="24" height="48" viewBox="0 0 24 48"><path d="M4 4l16 20L4 44" fill="none" stroke="rgba(255,255,255,.6)" stroke-width="3"/></svg>
  <div class="hero-title">ELECTRICAL<span class="dot">•</span>LED LIGHTING<span class="dot">•</span>SOLAR POWER</div>
  <div class="hero-sub"><span class="red">Australia's</span> Largest Fully Integrated <span class="red">Electrical &amp; Energy</span> Solutions Provider.</div>
</section>

<section class="welcome">
  <div class="welcome-logo">
    <div class="brand" style="position:static"><div class="brand-dot"></div><div class="brand-name">TAVO</div></div>
    <div class="brand-tag">Bright Days Ahead</div>
  </div>
  <div class="v-divider"></div>
  <h1 class="welcome-title">WELCOME TO <span class="red">TAVO</span> <small>Bright Days Ahead</small></h1>
  <p class="welcome-text">Tavo Electrical was formed to be an expert Electricity Contracting Company providing services to all Residential and Commercial Customers. With over 10 years of experience, Tavo Electrical has developed a highly-experienced team of professionals that ensure all our customer expectations are met.</p>
  <div class="btn-outline">READ MORE &nbsp;&gt;&gt;</div>
</section>

<div class="service" style="left:57px">
  <div class="photo" role="img" aria-label="Electrician in a hard hat working at a switchboard" style="background:linear-gradient(135deg,#c9c4b8,#8a8778)"></div>
  <h3>ELECTRICAL CONTRACTING</h3>
  <p>Lorem ipsum dolor sit amet, consectetuer adipiscing elit, tincidunt ut laoreet dolore magna aliquam erat volutpat.</p>
  <div class="toggle">+</div>
</div>
<div class="service" style="left:434px">
  <div class="photo" role="img" aria-label="Round LED high-bay light fitting" style="background:linear-gradient(135deg,#e6e6e6,#3a3a3a)"></div>
  <h3>LED LIGHTING UPGRADES</h3>
  <p>Lorem ipsum dolor sit amet, consectetuer adipiscing elit, tincidunt ut laoreet dolore magna aliquam erat volutpat.</p>
  <div class="toggle">+</div>
</div>
<div class="service" style="left:814px">
  <div class="photo" role="img" aria-label="Solar inverter in front of solar panels" style="background:linear-gradient(135deg,#3a4150,#1b1f28)"></div>
  <h3>SOLAR POWER</h3>
  <p style="color:var(--ink)">Lorem ipsum dolor sit amet, consectetuer adipiscing elit, tincidunt ut laoreet dolore magna aliquam erat volutpat.</p>
  <div class="toggle on">−</div>
</div>

<div class="section-rule" style="top:1484px"></div>

<h2 class="sec-title" style="top:1530px">WHY <span class="red">CHOOSE US ?</span></h2>

<svg class="abs" style="left:0;top:1640px" width="1200" height="60" viewBox="0 0 1200 60">
  <g fill="none" stroke="#ccc" stroke-width="2" stroke-dasharray="2 5">
    <path d="M200 40 Q256 10 312 36"/><path d="M428 36 Q485 60 542 36"/>
    <path d="M658 36 Q714 10 770 36"/><path d="M886 36 Q942 60 998 36"/>
  </g>
</svg>

<div class="feature" style="left:28px">
  <div class="icon"><svg width="44" height="44" viewBox="0 0 44 44"><circle cx="20" cy="12" r="8" fill="#222"/><path d="M4 40c0-10 7-16 16-16s16 6 16 16z" fill="#222"/><circle cx="34" cy="34" r="6" fill="#fff" stroke="#222" stroke-width="3"/></svg></div>
  <h4>PROFESSIONAL<br>SERVICE</h4>
  <p>Lorem ipsum dolor sit amet,<br>consectetuer elit..<b>(+)</b></p>
</div>
<div class="feature" style="left:255px">
  <div class="icon"><svg width="44" height="48" viewBox="0 0 44 48"><path d="M12 28l-6 18 8-4 4 6 4-16zM32 28l6 18-8-4-4 6-4-16z" fill="#222"/><circle cx="22" cy="18" r="15" fill="#222"/><circle cx="22" cy="18" r="10" fill="none" stroke="#fff" stroke-width="2"/><path d="M22 11l2 5h5l-4 3 2 5-5-3-5 3 2-5-4-3h5z" fill="#fff"/></svg></div>
  <h4>5 YEAR WORKMANSHIP<br>GUARANTEE</h4>
  <p>Lorem ipsum dolor sit amet,<br>consectetuer elit..<b>(+)</b></p>
</div>
<div class="feature" style="left:485px">
  <div class="icon"><svg width="44" height="48" viewBox="0 0 44 48"><path d="M15 4h14l-4 8h-6z" fill="#222"/><path d="M18 13h8c10 6 14 14 14 22 0 8-6 11-18 11S4 43 4 35c0-8 4-16 14-22z" fill="#222"/><text x="22" y="38" text-anchor="middle" font-family="Lato" font-weight="700" font-size="18" fill="#fff">$</text></svg></div>
  <h4>VALUE FOR<br>MONEY</h4>
  <p>Lorem ipsum dolor sit amet,<br>consectetuer elit..<b>(+)</b></p>
</div>
<div class="feature" style="left:712px">
  <div class="icon"><svg width="46" height="46" viewBox="0 0 46 46"><circle cx="23" cy="23" r="19" fill="none" stroke="#222" stroke-width="3"/><ellipse cx="23" cy="23" rx="8" ry="19" fill="none" stroke="#222" stroke-width="2.5"/><path d="M4 23h38M7 13h32M7 33h32" stroke="#222" stroke-width="2.5"/></svg></div>
  <h4>ENVIRONMENTALLY<br>FRIENDLY</h4>
  <p>Lorem ipsum dolor sit amet,<br>consectetuer elit..<b>(+)</b></p>
</div>
<div class="feature" style="left:942px">
  <div class="icon"><svg width="40" height="46" viewBox="0 0 40 46"><path d="M20 2l17 6v14c0 11-8 19-17 22C11 41 3 33 3 22V8z" fill="#222"/><path d="M11 23l6 6 12-12" fill="none" stroke="#fff" stroke-width="4"/></svg></div>
  <h4>FULLY<br>INSURED</h4>
  <p>Lorem ipsum dolor sit amet,<br>consectetuer elit..<b>(+)</b></p>
</div>

<div class="works-bg"></div>
<h2 class="sec-title" style="top:1935px">OUR <span class="red">WORKS</span></h2>

<div class="work" style="left:50px">
  <div class="card"><div class="mark" style="color:var(--red)">Velvetta</div><div class="photo" role="img" aria-label="Retail store interior with LED lighting" style="background:linear-gradient(180deg,#b9bcc2,#7b6f73)"></div></div>
  <h4>R. Malden</h4><div class="loc">( Balwyn North VIC )</div>
  <p>They clean up after the job, explained everything I needed to know and answered all questions, very professional. Will use them again in the future!</p>
</div>
<div class="work" style="left:425px">
  <div class="card"><div class="mark" style="color:#1e88c8">Steelmark</div><div class="photo" role="img" aria-label="Warehouse interior with high-bay lights" style="background:linear-gradient(180deg,#9aa0a8,#4e5259)"></div></div>
  <h4>Kestry</h4><div class="loc">( Cranbourne North VIC )</div>
  <p>Excellent work and very professional. Marcus takes time to explain everything and demonstrate workings. Very clear precise and accurate.</p>
</div>
<div class="work" style="left:800px">
  <div class="card"><div class="mark" style="color:#555;font-size:32px">BRIGHTWELL SIGNS</div><div class="photo" role="img" aria-label="Sign workshop floor under new lighting" style="background:linear-gradient(180deg,#c7c5bd,#6f6a5c)"></div></div>
  <h4>Paolo V.</h4><div class="loc">( Mount Waverley VIC )</div>
  <p>I found Marcus to be well organised, punctual, professional &amp; a good communicator. He did job a very reasonable price. A pleasure to deal with.</p>
</div>

<h2 class="sec-title" style="top:2520px">OUR <span class="red">SATISFIED CLIENTS</span></h2>
<svg class="client-arrow" style="left:18px" width="22" height="50" viewBox="0 0 22 50"><path d="M19 3L4 25l15 22" fill="none" stroke="#888" stroke-width="3"/></svg>
<div class="client outline" style="left:57px;width:229px">Velvetta</div>
<div class="client" style="left:325px;width:227px;border:none;background:#f4d21a;color:var(--ink);font-size:24px">Outback Surplus</div>
<div class="client solid" style="left:620px;width:232px">Heron Plumbing</div>
<div class="client solid" style="left:914px;width:232px;background:#d61f26">Golden Grill</div>
<svg class="client-arrow" style="right:14px" width="22" height="50" viewBox="0 0 22 50"><path d="M3 3l15 22L3 47" fill="none" stroke="#888" stroke-width="3"/></svg>

<div class="commit-bg"></div>
<h3 class="col-title" style="left:52px;width:520px">OUR <span class="red">COMMITMENT TO CUSTOMER</span></h3>
<p class="commit-text">Lorem autem vel eum iriure hendrerit in vulputate velit esse molestie. onsectetuer adipiscing elit, sed diam nonummy nibh euismod tincidunt u eu feugiat nulla facilisis.</p>
<ul class="ticks">
  <li><svg width="16" height="16" viewBox="0 0 16 16"><circle cx="8" cy="8" r="8" fill="#ec1f27"/><path d="M4 8l3 3 5-5" fill="none" stroke="#fff" stroke-width="2"/></svg>Autem vel eum iriure hendrerit in</li>
  <li><svg width="16" height="16" viewBox="0 0 16 16"><circle cx="8" cy="8" r="8" fill="#ec1f27"/><path d="M4 8l3 3 5-5" fill="none" stroke="#fff" stroke-width="2"/></svg>Gendrerit in vulputate velit</li>
  <li><svg width="16" height="16" viewBox="0 0 16 16"><circle cx="8" cy="8" r="8" fill="#ec1f27"/><path d="M4 8l3 3 5-5" fill="none" stroke="#fff" stroke-width="2"/></svg>Autem vel eum adipiscing elit, sed diam</li>
  <li><svg width="16" height="16" viewBox="0 0 16 16"><circle cx="8" cy="8" r="8" fill="#ec1f27"/><path d="M4 8l3 3 5-5" fill="none" stroke="#fff" stroke-width="2"/></svg>Eeum iriure hendrerit in vulputate velit</li>
</ul>

<h3 class="col-title" style="left:636px;width:512px">CLIENT <span class="red">TESTIMONIALS</span></h3>
<div class="quote-box"><span class="quote-mark">“</span>Lorem ipsum dolor sit amet consetug e sed diay nibh euismodl tincidunt ut laoreet dolore magam er vol wisi enim ad minim veniam quis nostrud exerci tationorem ipsum dolor sit ametee sed diammmy nibh euismod tincidunt ut laoreet dolore magna aliqur volpatl tiidunt ut laoreet dolore magna aliqur volpatl r sit ametee.</div>
<div class="avatar" role="img" aria-label="Client portrait"></div>
<div class="client-name">Mrs. Clara Whitby</div>

<footer>
  <div class="footer-nav">
    <div class="footer-links"><span>HOME</span><span>TAVO STORY</span><span>SERVICES</span><span>OUR WORK</span><span>CONTACT US</span></div>
    <div class="social"><span aria-label="Social profile one">FB</span><span aria-label="Social profile two">TW</span><span aria-label="Social profile three">YT</span></div>
  </div>
  <div class="footer-main">
    <div class="f-item" style="left:52px">
      <div class="f-icon"><svg width="14" height="18" viewBox="0 0 14 18"><path d="M7 0a7 7 0 0 0-7 7c0 5 7 11 7 11s7-6 7-11a7 7 0 0 0-7-7z" fill="#ec1f27"/><circle cx="7" cy="7" r="2.5" fill="#2b2b2b"/></svg></div>
      <div><b>TAVO</b> - bright days ahead<br>12/84 ellery st mount waverley vic 3149</div>
    </div>
    <div class="f-item" style="left:470px">
      <div class="f-icon"><svg width="16" height="16" viewBox="0 0 24 24"><path fill="#ec1f27" d="M6.6 10.8a15 15 0 0 0 6.6 6.6l2.2-2.2a1 1 0 0 1 1-.25 11.4 11.4 0 0 0 3.6.57 1 1 0 0 1 1 1V20a1 1 0 0 1-1 1A17 17 0 0 1 3 4a1 1 0 0 1 1-1h3.5a1 1 0 0 1 1 1c0 1.25.2 2.45.57 3.57a1 1 0 0 1-.25 1z"/></svg></div>
      <div><b>Call Us :</b><br>138420</div>
    </div>
    <div class="f-item" style="left:660px">
      <div class="f-icon"><svg width="16" height="12" viewBox="0 0 18 14"><rect x="1" y="1" width="16" height="12" fill="none" stroke="#ec1f27" stroke-width="1.8"/><path d="M1 1l8 7 8-7" fill="none" stroke="#ec1f27" stroke-width="1.8"/></svg></div>
      <div><b>Email Us :</b><br>service@tavoelectrical.com.au</div>
    </div>
    <div class="f-brand"><div class="name">TAVO</div><div class="tag">Bright Days Ahead</div></div>
  </div>
  <div class="copyright">Copyright © 2017 Tavo. All Right Reserved.</div>
</footer>

</body>
</html>
```